Corvane Bookkeeping Services business cards

looking for a double sided business card design. My logo is attached. I am looking for a design similar to the attached. Keen to see what my logo in white on the blue background would look like.

```html
<!DOCTYPE html>
<html lang="en">
<head>
<meta charset="utf-8">
<title>Corvane Bookkeeping Services – Business Cards</title>
<link href="https://fonts.googleapis.com/css2?family=Montserrat:wght@700;800&family=Poppins:wght@300;400&display=swap" rel="stylesheet">
<style>
  :root {
    --backdrop: #737373;
    --navy: #003469;
    --green: #8db52f;
    --white: #ffffff;
    --text-grey: #555555;
    --ink: #222222;
    --faint: #e3e3e3;
  }
  * { margin: 0; padding: 0; box-sizing: border-box; }
  html, body { width: 1200px; height: 1000px; overflow: hidden; }
  body { background: var(--backdrop); position: relative; font-family: "Poppins", sans-serif; }

  .card { position: absolute; border-radius: 22px; overflow: hidden; }

  .card-front {
    left: 293px; top: 95px; width: 613px; height: 350px;
    background: var(--navy);
    display: flex; align-items: center; justify-content: center;
  }
  .front-brand {
    display: flex; align-items: center; gap: 18px;
  }
  .front-brand .brand-square {
    flex: none; width: 64px; height: 64px; background: var(--white);
  }
  .front-brand .brand-name {
    font-family: "Montserrat", sans-serif; font-weight: 800;
    color: var(--white); font-size: 30px; line-height: 1.15;
    white-space: nowrap;
  }

  .card-back {
    left: 291px; top: 503px; width: 614px; height: 352px;
    background: var(--white);
  }
  .back-mark {
    position: absolute; left: 330px; top: 20px; width: 250px; height: 250px;
    border-radius: 50%; background: var(--faint);
  }
  .back-brand {
    position: absolute; left: 39px; top: 68px;
    font-family: "Montserrat", sans-serif; font-weight: 800;
    color: var(--navy); font-size: 20px; line-height: 1.2;
    white-space: nowrap;
  }
  .holder { position: absolute; left: 39px; top: 174px; }
  .holder-name {
    font-family: "Montserrat", sans-serif; font-weight: 700;
    color: var(--navy); font-size: 21px; letter-spacing: 0.2px;
  }
  .holder-role { font-weight: 300; color: var(--ink); font-size: 16px; }

  .contact-list { position: absolute; left: 41px; top: 263px; list-style: none; }
  .contact-list li {
    display: flex; align-items: center; gap: 9px;
    font-weight: 300; color: var(--text-grey); font-size: 15px; line-height: 19.5px;
    white-space: nowrap;
  }
  .contact-list svg { width: 14px; height: 14px; flex: none; }

  .postal {
    position: absolute; right: 36px; top: 284px; text-align: right;
    font-style: normal; font-weight: 300; color: var(--text-grey);
    font-size: 15px; line-height: 19.5px; white-space: nowrap;
  }
</style>
</head>
<body>
  <section class="card card-front">
    <div class="front-brand">
      <span class="brand-square"></span>
      <span class="brand-name">Corvane<br>Bookkeeping Services</span>
    </div>
  </section>

  <section class="card card-back">
    <div class="back-mark"></div>
    <div class="back-brand">Corvane<br>Bookkeeping Services</div>

    <div class="holder">
      <div class="holder-name">DANIEL WHITMORE</div>
      <div class="holder-role">Founder</div>
    </div>

    <ul class="contact-list">
      <li>
        <svg viewBox="0 0 14 14" aria-hidden="true"><rect x="3.5" y="0.8" width="7" height="12.4" rx="1.2" fill="none" stroke="var(--green)" stroke-width="1.6"/><rect x="6" y="10.4" width="2" height="1.2" fill="var(--green)"/></svg>
        0400 318 276
      </li>
      <li>
        <svg viewBox="0 0 14 14" aria-hidden="true"><rect x="0.5" y="2.5" width="13" height="9" fill="var(--green)"/><path d="M0.5 2.8 L7 8 L13.5 2.8" fill="none" stroke="var(--white)" stroke-width="1.2"/></svg>
        hello@corvanebookkeeping.com.au
      </li>
      <li>
        <svg viewBox="0 0 14 14" aria-hidden="true"><circle cx="7" cy="7" r="6" fill="none" stroke="var(--green)" stroke-width="1.4"/><ellipse cx="7" cy="7" rx="2.6" ry="6" fill="none" stroke="var(--green)" stroke-width="1.2"/><path d="M1 7 H13 M2 4 H12 M2 10 H12" stroke="var(--green)" stroke-width="1.1"/></svg>
        corvanebookkeeping.com.au
      </li>
    </ul>

    <address class="postal">PO Box 4721, Ellerby<br>Queensland 4399</address>
  </section>
</body>
</html>
```